Luxury free range egg pack for eggs with golden orange yolks

We are looking for a new faced egg pack for one of our brands called Meadow Crest which is free range eggs with golden yolks.
This will be for a more up market target audience.

Target Market(s)

Luxury egg purchase

Industry/Entity Type

Egg production

Font styles to use
Decorative
Script

Colors
F0912C
F2A743
F7CA91
FBE8D2
FDF5EE

Requirements
Must have
• Orange or gold colouring in place in the theme

```html
<!DOCTYPE html>
<html lang="en">
<head>
<meta charset="utf-8">
<title>Meadow Crest – Free Range Egg Pack</title>
<link rel="stylesheet" href="https://fonts.googleapis.com/css2?family=Archivo+Black&display=swap">
<style>
  :root {
    --burnt-orange: #E5651A;
    --pack-orange: #F0912C;
    --warm-gold: #F2A743;
    --soft-apricot: #F7CA91;
    --cream: #FBE8D2;
    --shell-white: #FDF5EE;
    --ink-white: #FFFFFF;
  }
  html, body {
    margin: 0;
    padding: 0;
    width: 720px;
    height: 1200px;
    overflow: hidden;
    background: var(--shell-white);
  }
  .pack {
    position: relative;
    width: 720px;
    height: 1200px;
    overflow: hidden;
    font-family: "Archivo Black", "Arial Black", sans-serif;
    color: var(--ink-white);
  }
  .top-band {
    position: absolute;
    left: 0; top: 0;
    width: 720px; height: 150px;
    background: var(--burnt-orange);
  }
  .main-panel {
    position: absolute;
    left: 0; top: 150px;
    width: 720px; height: 758px;
    background: var(--pack-orange);
  }
  .grass {
    position: absolute;
  }
  .grass--left {
    left: 0; top: 470px;
    width: 150px; height: 438px;
    border-radius: 0 150px 0 0;
    background: linear-gradient(90deg, var(--shell-white) 0%, var(--cream) 30%, var(--soft-apricot) 60%, rgba(247,202,145,0) 100%);
    opacity: 0.8;
  }
  .grass--right {
    right: 0; top: 345px;
    width: 130px; height: 380px;
    border-radius: 130px 0 0 0;
    background: linear-gradient(270deg, var(--shell-white) 0%, var(--cream) 30%, var(--soft-apricot) 60%, rgba(247,202,145,0) 100%);
    opacity: 0.8;
  }
  .brand-name,
  .brand-sub,
  .tagline {
    position: absolute;
    left: 0;
    width: 720px;
    margin: 0;
    text-align: center;
    line-height: 1;
    white-space: nowrap;
  }
  .brand-name {
    top: 219px;
    left: -8px;
    font-size: 120px;
  }
  .brand-sub {
    top: 342px;
    left: 14px;
    font-size: 94px;
  }
  .tagline {
    font-size: 48px;
  }
  .tagline--first { top: 535px; left: -8px; }
  .tagline--second { top: 601px; left: -4px; }
  .pattern-band {
    position: absolute;
    left: 0; top: 908px;
    width: 720px; height: 236px;
    background:
      linear-gradient(90deg, rgba(240,145,44,0.55) 0%, rgba(253,245,238,0) 25%, rgba(240,145,44,0.55) 50%, rgba(253,245,238,0) 75%, rgba(240,145,44,0.55) 100%),
      linear-gradient(180deg, var(--cream) 0%, var(--soft-apricot) 50%, var(--warm-gold) 100%);
  }
  .bottom-band {
    position: absolute;
    left: 0; top: 1144px;
    width: 720px; height: 56px;
    background: var(--burnt-orange);
  }
  .bottom-band__text {
    margin: 0;
    padding-top: 18px;
    padding-left: 10px;
    text-align: center;
    font-size: 17.4px;
    letter-spacing: 0.6px;
    line-height: 1;
    white-space: nowrap;
  }
</style>
</head>
<body>
  <main class="pack">
    <div class="top-band"></div>
    <section class="main-panel"></section>
    <div class="grass grass--left" role="img" aria-label="Stylised cream grass blades rising from the lower left"></div>
    <div class="grass grass--right" role="img" aria-label="Stylised cream grass blades along the right edge"></div>

    <h1 class="brand-name">MEADOW</h1>
    <p class="brand-sub">CREST</p>
    <p class="tagline tagline--first">EGGS WITH</p>
    <p class="tagline tagline--second">GOLDEN YOLKS</p>

    <div class="pattern-band" role="img" aria-label="Orange and cream harlequin diamond pattern"></div>

    <footer class="bottom-band">
      <p class="bottom-band__text">WEST COUNTRY FREE RANGE EGGS WITH EXTRA RICH YOLKS</p>
    </footer>
  </main>
</body>
</html>
```